Freelance Translator in Need of a Business Card

I am a freelance Japanese to English translator. I work in the video game localization industry and do literary translation in my spare time. I would like to have both the English word 'Translator' and the Japanese '翻訳者' in the job title. The final design should evoke trust, openness, and reliability.

Target Market(s)

Video game localization companies
Japanese comic book artists

Industry/Entity Type

Business

Contact Information for Business Card

Daniel Oskerby, Translator
dan.oskerby@fernlowmail.com
velmotranslates.com
twitter: @velmo_tl

Colors

Designer to choose colors to be used in the design.

```html
<!DOCTYPE html>
<html lang="en">
<head>
<meta charset="utf-8">
<title>Daniel Oskerby – Translator Business Card</title>
<link href="https://fonts.googleapis.com/css2?family=Courier+Prime:wght@400;700&family=Noto+Serif+JP:wght@400&display=swap" rel="stylesheet">
<style>
  :root {
    --backdrop: #d9d9d9;
    --card: #1c1c1c;
    --ink-light: #f2f2f2;
    --accent: #5f7089;
    --rule-light: #f4f4f4;
    --icon: #5f7089;
  }
  * { margin: 0; padding: 0; box-sizing: border-box; }
  html, body {
    width: 1200px; height: 1200px; overflow: hidden;
    background: var(--backdrop);
  }
  .canvas { position: relative; width: 1200px; height: 1200px; }
  .card {
    position: absolute; left: 150px;
    width: 900px; height: 514px;
    background: var(--card);
    font-family: "Courier Prime", "Courier New", monospace;
    color: var(--ink-light);
  }
  .card--back { top: 50px; }
  .card--front { top: 636px; }

  .card__rule {
    position: absolute; left: 0; right: 0; top: 410px; height: 5px;
    display: flex;
  }
  .card__rule-accent { width: 46%; background: var(--accent); }
  .card__rule-light { flex: 1; background: var(--rule-light); }

  .back__name {
    position: absolute; left: 0; right: 0; top: 210px;
    text-align: center;
    font-size: 38px; letter-spacing: 6px; font-weight: 400;
    padding-left: 120px;
  }

  .front__identity { position: absolute; left: 70px; top: 90px; }
  .front__name {
    font-size: 36px; letter-spacing: 6px; line-height: 1; font-weight: 400;
  }
  .front__title {
    margin-top: 6px;
    display: flex; align-items: baseline; gap: 16px;
    font-size: 24px; letter-spacing: 3px; color: var(--accent);
  }
  .front__title-ja {
    font-family: "Noto Serif JP", serif;
    font-size: 21px; letter-spacing: 3px; font-weight: 400;
  }

  .front__contacts {
    position: absolute; left: 380px; top: 250px;
    list-style: none;
    font-size: 21px; letter-spacing: 1.5px;
  }
  .front__contacts li {
    display: flex; align-items: center; gap: 14px;
    height: 34px;
  }
  .contact__icon { width: 22px; height: 22px; flex: none; }
</style>
</head>
<body>
<main class="canvas">

  <section class="card card--back" aria-label="Card back">
    <h2 class="back__name">DANIEL OSKERBY</h2>
    <div class="card__rule"><span class="card__rule-accent"></span><span class="card__rule-light"></span></div>
  </section>

  <section class="card card--front" aria-label="Card front">
    <div class="front__identity">
      <h1 class="front__name">DANIEL OSKERBY</h1>
      <p class="front__title"><span>TRANSLATOR</span><span class="front__title-ja" lang="ja">翻訳者</span></p>
    </div>

    <ul class="front__contacts">
      <li>
        <svg class="contact__icon" viewBox="0 0 22 22" aria-hidden="true">
          <rect x="2" y="5" width="18" height="12" fill="none" stroke="var(--icon)" stroke-width="2"/>
          <path d="M2 5 L11 12 L20 5" fill="none" stroke="var(--icon)" stroke-width="2"/>
        </svg>
        <span>dan.oskerby@fernlowmail.com</span>
      </li>
      <li>
        <svg class="contact__icon" viewBox="0 0 22 22" aria-hidden="true">
          <circle cx="11" cy="11" r="9" fill="none" stroke="var(--icon)" stroke-width="2"/>
          <ellipse cx="11" cy="11" rx="4" ry="9" fill="none" stroke="var(--icon)" stroke-width="1.5"/>
          <line x1="2" y1="11" x2="20" y2="11" stroke="var(--icon)" stroke-width="1.5"/>
        </svg>
        <span>velmotranslates.com</span>
      </li>
      <li>
        <svg class="contact__icon" viewBox="0 0 22 22" aria-hidden="true">
          <circle cx="11" cy="11" r="8" fill="var(--icon)"/>
        </svg>
        <span>@velmo_tl</span>
      </li>
    </ul>

    <div class="card__rule"><span class="card__rule-accent"></span><span class="card__rule-light"></span></div>
  </section>

</main>
</body>
</html>
```